Branding for Velēra Cider a new Tasmanian cider company

We are a new Tasmanian cider business looking for a logo/label design to be used on our 330ml cider bottle labels and as a logo.
We want our cider label to pop and stand out from the rest.
As our cider is a Tasmanian product we would like it to appear as a premium product.
I have attached pictures of all of the other Tasmanian Cider labels to give an idea of what we are competing with NOT because we like the designs!!!

We are yet to start advertising our business so it is all an open slab, we have no starting point just a few ideas that have been listed below in the "Nice to Haves" section.

This brief has been updated as what we originally requested was too similar to other labels already in production so didn't give our product an edge.

The label size will be approx 80mm x 125mm

Target Market(s)

Craft cider market, bottle shops, boutique bars and restaurants

Font styles to use
Serif
Decorative
Script

Colors

Designer to choose colors to be used in the design.

Requirements
Must have
• The words
• "Velēra Cider" with the diacritic's over the o's
• "Tasmanian Made"
• or
• "Made in Tasmania"
• The Tasmanian part can be in all caps if it looks better
Nice to have
• All or some of the below incorporated into the label:
• Velēra was the goddess of fruit trees, gardens, and orchards.
• She watched over and protected fruit trees
• She was thought to be a wood nymph which are usually represented as beautiful, young girls.
• We would like our label to possibly incorporate the above.
• Maybe a wood nymph/goddess in an apple/pear orchard or against an apple/pear tree.
• Maybe no tree, just the nymph/goddess holding fruit.
• Maybe an apple/pear branch with a nympy/goddess under it.
• I have attached a few images from searchly of wood nymphs and fruit goddess' for inspiration. Not sure if realistic or animated would look best, but if animated, not cartoon like as we would like a premium look. Possibly similar to the attached Torvik Cider artwork
• We will have 3 types of cider; Apple, Pear and Apple & Strawberry so essentially 3 labels, maybe the apple tree could change to a pear tree and for the apple & strawberry cider maybe strawberries growing under the apple tree?
• All just ideas, we are open to :)
• If you think something else will suit the name, please feel free to submit it

```html
<!DOCTYPE html>
<html lang="en">
<head>
<meta charset="utf-8">
<title>Velēra Cider – Labels</title>
<link href="https://fonts.googleapis.com/css2?family=Playfair+Display:wght@900&family=Cormorant+Garamond:wght@500;600&family=Great+Vibes&display=swap" rel="stylesheet">
<style>
  :root {
    --page: #ffffff;
    --label-bg: #fdfcf8;
    --label-edge: #c9c9c9;
    --ink: #111111;
    --body-ink: #2b2b2b;
    --strawberry: #e0245e;
    --apple: #6cc24a;
    --apple-deep: #4f9a2c;
    --berry-red: #d8262c;
  }
  * { margin: 0; padding: 0; box-sizing: border-box; }
  html, body { width: 1200px; height: 802px; overflow: hidden; background: var(--page); }
  .sheet { position: relative; width: 1200px; height: 802px; }

  .label {
    position: absolute;
    top: 29px;
    width: 547px;
    height: 739px;
    background: var(--label-bg);
    border: 1.5px solid var(--label-edge);
    text-align: center;
  }
  .label--strawberry { left: 29px; --accent: var(--strawberry); }
  .label--apple { left: 624px; --accent: var(--apple); }

  .fruit-art {
    position: absolute;
    left: 138px;
    top: 72px;
    width: 270px;
    height: 245px;
    border-radius: 46%;
  }
  .label--strawberry .fruit-art {
    background:
      radial-gradient(ellipse 55% 45% at 50% 72%, var(--berry-red) 0%, rgba(216,38,44,0.85) 45%, rgba(216,38,44,0) 75%),
      radial-gradient(ellipse 48% 50% at 50% 38%, #8fd35a 0%, var(--apple-deep) 70%, rgba(79,154,44,0) 100%);
  }
  .label--apple .fruit-art {
    background:
      radial-gradient(ellipse 30% 42% at 66% 52%, #f3f6e6 0%, #dfeabf 60%, rgba(223,234,191,0) 100%),
      radial-gradient(ellipse 52% 52% at 45% 50%, #9ad865 0%, var(--apple-deep) 72%, rgba(79,154,44,0) 100%);
  }

  .rule {
    position: absolute;
    left: 115px;
    width: 336px;
    height: 4px;
    background: var(--accent);
  }
  .rule--top { top: 328px; }
  .rule--bottom { top: 474px; }
  .label--apple .rule--bottom { display: none; }

  .brand {
    position: absolute;
    top: 332px;
    left: 0;
    width: 100%;
    font-family: "Playfair Display", serif;
    font-weight: 900;
    font-size: 48px;
    line-height: 68px;
    letter-spacing: 1px;
    color: var(--ink);
  }

  .flavour {
    position: absolute;
    top: 490px;
    left: 0;
    width: 100%;
    font-family: "Cormorant Garamond", serif;
    font-weight: 600;
    font-size: 30px;
    line-height: 36px;
    letter-spacing: 1px;
    color: var(--ink);
  }
  .label--apple .flavour { top: 482px; font-size: 33px; }

  .blurb {
    position: absolute;
    top: 549px;
    left: 105px;
    width: 337px;
    font-family: "Cormorant Garamond", serif;
    font-weight: 500;
    font-size: 19px;
    line-height: 24px;
    color: var(--body-ink);
  }

  .origin {
    position: absolute;
    top: 632px;
    left: 0;
    width: 100%;
    font-family: "Great Vibes", cursive;
    font-size: 28px;
    line-height: 34px;
    color: var(--accent);
  }

  .volume {
    position: absolute;
    top: 675px;
    left: 0;
    width: 100%;
    font-family: "Cormorant Garamond", serif;
    font-weight: 600;
    font-size: 17px;
    line-height: 22px;
    color: var(--body-ink);
  }
</style>
</head>
<body>
<main class="sheet">

  <article class="label label--strawberry">
    <div class="fruit-art" role="img" aria-label="Photograph of a green apple with ripe strawberries and leaves"></div>
    <div class="rule rule--top"></div>
    <h1 class="brand">VELĒRA<br>CIDER</h1>
    <div class="rule rule--bottom"></div>
    <p class="flavour">APPLE &amp; STRAWBERRY</p>
    <p class="blurb">Lorem ipsum dolor sit amet, consectetur adipiscing elit, sed do eiusmod tempor incididunt ut labore</p>
    <p class="origin">Made in Tasmania</p>
    <p class="volume">330mL</p>
  </article>

  <article class="label label--apple">
    <div class="fruit-art" role="img" aria-label="Photograph of a whole green apple and a halved green apple with leaves"></div>
    <div class="rule rule--top"></div>
    <h1 class="brand">VELĒRA<br>CIDER</h1>
    <div class="rule rule--bottom"></div>
    <p class="flavour">APPLE</p>
    <p class="blurb">Lorem ipsum dolor sit amet, consectetur adipiscing elit, sed do eiusmod tempor incididunt ut labore</p>
    <p class="origin">Made in Tasmania</p>
    <p class="volume">330mL</p>
  </article>

</main>
</body>
</html>
```